http://www.lanternfieldcollective.org/

would like someone to rebuild this -http://www.lanternfieldcollective.com/ to be more modern and more easily updated

Industry/Entity Type

Non Profit

Coding

Coded - Design and coding required

Colors

Designer to choose colors to be used in the design.

Requirements
Must have
• use of the logo, and a newer design for wordpress to be hosted on Azure and easily updated templates

```html
<!DOCTYPE html>
<html lang="en">
<head>
<meta charset="utf-8">
<title>Lanternfield Collective</title>
<link rel="stylesheet" href="https://fonts.googleapis.com/css2?family=Lora:ital,wght@0,400;0,700;1,400;1,700&family=Montserrat:wght@500;600;700&family=Open+Sans:wght@400;600&display=swap">
<style>
:root{
  --ink:#1f1d24;
  --plum:#2e2646;
  --plum-deep:#2b2342;
  --plum-soft:#3a3060;
  --line:#2e2a5e;
  --grey:#efefef;
  --text:#333;
  --muted:#8a8a8a;
  --link:#3a4fd0;
  --sky:#a8d0dc;
  --white:#fff;
}
*{margin:0;padding:0;box-sizing:border-box}
html,body{width:1200px;height:2500px;overflow:hidden;background:var(--white)}
body{position:relative;font-family:"Open Sans",Arial,sans-serif;color:var(--text)}
.abs{position:absolute}
.serif{font-family:"Lora",Georgia,serif}
.sans{font-family:"Montserrat",Arial,sans-serif}

/* header */
.header{left:0;top:0;width:1200px;height:78px;background:var(--white);z-index:3}
.brand{left:238px;top:8px;width:94px;height:94px;border-radius:50%;background:var(--white);border:3px solid var(--plum);display:flex;align-items:center;justify-content:center;text-align:center;z-index:4}
.brand span{font-family:"Lora",Georgia,serif;font-weight:700;font-size:11px;line-height:13px;color:var(--plum)}
.nav{left:370px;top:35px;display:flex;gap:16px;font-family:"Montserrat",Arial,sans-serif;font-weight:600;font-size:8.6px;color:var(--ink);letter-spacing:.1px}
.btn-top{left:859px;top:22px;width:107px;height:35px;background:var(--plum);color:var(--white);font-family:"Montserrat",Arial,sans-serif;font-weight:600;font-size:10px;display:flex;align-items:center;justify-content:center;border-radius:2px}

/* hero */
.hero{left:0;top:78px;width:1200px;height:344px;background:linear-gradient(90deg,#6d7a2a 0%,#9aa23a 35%,#b8a04a 60%,#d6b48a 78%,#8e7a3a 100%)}
.hero-title{left:235px;top:175px;font-family:"Lora",Georgia,serif;font-style:italic;font-weight:700;font-size:33px;line-height:38px;color:var(--white)}
.btn-pill{left:235px;top:277px;width:150px;height:39px;border-radius:20px;background:var(--plum);color:var(--white);font-family:"Montserrat",Arial,sans-serif;font-weight:600;font-size:12.5px;display:flex;align-items:center;justify-content:center}
.round-arrow{width:34px;height:34px;border-radius:50%;background:rgba(20,20,25,.85);display:flex;align-items:center;justify-content:center}
.zigzag{left:0;width:1200px;height:6px}

/* section heads */
.rule{left:141px;width:62px;height:2px;background:var(--line)}
.label{left:235px;font-family:"Montserrat",Arial,sans-serif;font-weight:600;font-size:14px;color:var(--line)}
.title{left:235px;font-family:"Lora",Georgia,serif;font-size:22px;color:var(--ink)}
.sq-arrows{display:flex;gap:2px}
.sq-arrows div{width:24px;height:24px;background:#7d7d7d;display:flex;align-items:center;justify-content:center}

/* about */
.about-text{left:235px;top:586px;width:380px;font-size:8.8px;line-height:15px;color:#222}
.about-link{left:235px;top:692px;font-size:8.8px;font-style:italic;color:var(--link);text-decoration:underline}
.quote{left:235px;font-family:"Lora",Georgia,serif;font-style:italic;font-size:10px;line-height:15px;color:#222}
.portrait{left:653px;top:513px;width:313px;height:316px;background:linear-gradient(160deg,#c9a24a,#7a1f20 55%,#3b2a22)}
.caption{left:653px;top:843px;width:313px;text-align:center;font-family:"Lora",Georgia,serif;font-style:italic;font-size:12px;color:#222}
.town-left{left:0;top:620px;width:400px;height:290px;background:radial-gradient(ellipse at 30% 60%,rgba(196,170,140,.55),rgba(170,190,210,.25) 55%,rgba(255,255,255,0) 75%)}
.town-right{left:1130px;top:620px;width:70px;height:270px;background:radial-gradient(ellipse at 70% 55%,rgba(140,170,200,.55),rgba(255,255,255,0) 70%)}

/* projects */
.letter{top:1008px;width:231px;height:176px;border:3px solid var(--plum);background:linear-gradient(180deg,#f7f6f2,#ecebe6)}

/* donation */
.hands{left:0;top:1242px;width:609px;height:366px;background:linear-gradient(135deg,#3b3a4a,#6b6070 40%,#9c8a86 60%,#5a6a8a)}
.donate-panel{left:609px;top:1242px;width:591px;height:366px;background:var(--grey)}
.kicker{left:653px;top:1302px;font-family:"Lora",Georgia,serif;font-style:italic;font-size:15px;color:var(--ink)}
.big{left:653px;top:1333px;font-family:"Montserrat",Arial,sans-serif;font-weight:700;font-size:31px;line-height:37px;color:var(--ink);letter-spacing:.5px}
.donate-text{left:653px;top:1413px;width:315px;font-size:8.8px;line-height:16.3px;color:#333}
.btn-sq{width:134px;height:47px;display:flex;align-items:center;justify-content:center;gap:8px;font-family:"Montserrat",Arial,sans-serif;font-weight:600;font-size:10.5px;letter-spacing:1.4px;color:var(--white)}

/* blog */
.post{top:1758px;width:232px}
.post .photo{height:139px;position:relative}
.badge{position:absolute;left:7px;bottom:8px;height:21px;background:var(--plum);color:var(--white);font-family:"Montserrat",Arial,sans-serif;font-weight:600;font-size:8px;display:flex;align-items:center;gap:10px;padding:0 8px}
.post h3{margin-top:14px;font-family:"Montserrat",Arial,sans-serif;font-weight:600;font-size:11px;color:var(--ink)}
.post p{margin-top:6px;font-size:8.6px;line-height:15px;color:var(--muted)}
.post .more{margin-top:10px;font-family:"Montserrat",Arial,sans-serif;font-weight:600;font-size:8px;color:#333}

/* footer */
.foot-band{left:0;top:2068px;width:1200px;height:78px;background:var(--plum)}
.newsletter{left:466px;top:2068px;width:268px;height:78px;background:var(--plum-soft)}
.foot-brand{left:301px;top:2041px;width:98px;height:98px}
.mail-ph{left:507px;top:2102px;font-size:8.5px;color:#a9a3c0}
.submit{left:661px;top:2101px;font-family:"Montserrat",Arial,sans-serif;font-weight:600;font-size:9.5px;color:var(--white)}
.socials{left:778px;top:2102px;display:flex;gap:24px}
.socials span{width:10px;height:10px;border-radius:50%;background:var(--white);display:block}
.foot-main{left:0;top:2146px;width:1200px;height:354px;background:var(--plum-deep)}
.foot-head{top:2196px;font-family:"Montserrat",Arial,sans-serif;font-weight:700;font-size:11.5px;color:var(--white)}
.foot-text{font-size:8.5px;line-height:17px;color:#e8e6ef}
.vline{top:2185px;width:1px;height:200px;background:#463d63}
.feed{left:488px;top:2238px;display:grid;grid-template-columns:repeat(4,56px);grid-template-rows:repeat(2,56px);gap:1px}
.links{left:767px;top:2232px;font-size:8.5px;line-height:19px;color:#e8e6ef;list-style:none}
.hline{left:0;top:2445px;width:1200px;height:1px;background:#3f365c}
.copy{left:0;top:2467px;width:1200px;text-align:center;font-size:8.5px;color:#e8e6ef}
</style>
</head>
<body>

<header class="abs header">
  <div class="abs brand"><span>Lanternfield<br>Collective</span></div>
  <nav class="abs nav">
    <span>HOME</span><span>ABOUT US</span><span>PROJECTS</span><span>NEWSLETTER &amp; REPORTS</span><span>MEDIA</span><span>WHAT;S NEW</span><span>CONTACT US</span>
  </nav>
  <div class="abs btn-top">DONATE NOW</div>
</header>

<section>
  <div class="abs hero" role="img" aria-label="Photo of a woman praying outdoors with folded hands"></div>
  <h1 class="abs hero-title">Helping Needy Christian<br>Widows and Orphans</h1>
  <div class="abs btn-pill">DONATE NOW</div>
  <div class="abs round-arrow" style="left:100px;top:242px"><svg width="12" height="12" viewBox="0 0 12 12"><path d="M8 1 3 6l5 5" fill="none" stroke="#fff" stroke-width="2"/></svg></div>
  <div class="abs round-arrow" style="left:1060px;top:242px"><svg width="12" height="12" viewBox="0 0 12 12"><path d="M4 1l5 5-5 5" fill="none" stroke="#fff" stroke-width="2"/></svg></div>
  <svg class="abs zigzag" style="top:418px" viewBox="0 0 1200 6" preserveAspectRatio="none">
    <defs><pattern id="zz" width="6" height="6" patternUnits="userSpaceOnUse"><path d="M0 6 3 0 6 6z" fill="#fff"/></pattern></defs>
    <rect width="1200" height="6" fill="url(#zz)"/>
  </svg>
</section>

<section>
  <div class="abs town-left" role="img" aria-label="Watercolor illustration of old town buildings"></div>
  <div class="abs town-right" role="img" aria-label="Watercolor illustration of a bell tower"></div>
  <div class="abs rule" style="top:538px"></div>
  <div class="abs label" style="top:528px">ABOUT US</div>
  <h2 class="abs title" style="top:550px">Lanternfield Collective</h2>
  <p class="abs about-text">Then the King will say to those on His right hand, ‘Come, you blessed of My Father, inherit the kingdom prepared for you from the foundation of the world: for I was hungry and you gave Me food; I was thirsty and you gave Me drink; I was a stranger and you took Me in; I was naked and you clothed Me; I was sick and you visited Me; I was in prison and you came to Me.’ “Assuredly, I say to you, inasmuch as you did it to one of the least of these My brethren, you did it to Me.”</p>
  <p class="abs about-link">Click here to read or download our latest letter for April, 2019.</p>
  <p class="abs quote" style="top:735px">“May God protect and lead in peace our shepherd,<br>Father Elias Morrow.</p>
  <p class="abs quote" style="top:780px">We pray to our Lord God and Savior Jesus Christ to keep him.<br>Pray for us.”</p>
  <div class="abs portrait" role="img" aria-label="Photo of a church leader in ceremonial vestments holding a staff"></div>
  <p class="abs caption">Father Elias Morrow</p>
</section>

<section>
  <div class="abs rule" style="top:944px"></div>
  <div class="abs label" style="top:934px">PROJECTS</div>
  <h2 class="abs title" style="top:956px">Letters from Egypt</h2>
  <div class="abs sq-arrows" style="left:916px;top:941px">
    <div><svg width="8" height="8" viewBox="0 0 8 8"><path d="M5.5 1 2.5 4l3 3" fill="none" stroke="#fff" stroke-width="1.4"/></svg></div>
    <div><svg width="8" height="8" viewBox="0 0 8 8"><path d="M2.5 1l3 3-3 3" fill="none" stroke="#fff" stroke-width="1.4"/></svg></div>
  </div>
  <div class="abs letter" style="left:234px" role="img" aria-label="Scanned typed letter of thanks in Arabic"></div>
  <div class="abs letter" style="left:484px" role="img" aria-label="Scanned handwritten letter of thanks in Arabic"></div>
  <div class="abs letter" style="left:734px;background:linear-gradient(180deg,#6a5f8a 0,#6a5f8a 22%,#f4f3ef 22%)" role="img" aria-label="Scanned handwritten letter on letterhead paper"></div>
</section>

<section>
  <div class="abs hands" role="img" aria-label="Photo of many hands stacked together"></div>
  <div class="abs donate-panel"></div>
  <p class="abs kicker">Where to find us</p>
  <h2 class="abs big">MAKE A<br>DONATION</h2>
  <p class="abs donate-text">Dolor sit amet, consectetur adipiscing elit, sed do eiusmo tempor incididunt ut labore et dolore magna aliqua. Ut enim ad minim veniam, quis nostrud exercitation ullamo laboris nisi ut aliquip ex ea commodo consequat. Duis aute irure dolor in reprehenderit in voluptate velit esse.</p>
  <div class="abs btn-sq" style="left:653px;top:1492px;background:var(--plum)">
    <svg width="16" height="14" viewBox="0 0 16 14"><path d="M8 3.5C7 1 3.5 1 3.5 4c0 2.5 4.5 5 4.5 5s4.5-2.5 4.5-5c0-3-3.5-3-4.5-.5zM1 12h5l3 1 6-2" fill="none" stroke="#fff" stroke-width="1"/></svg>
    DONATE
  </div>
  <svg class="abs zigzag" style="top:1604px" viewBox="0 0 1200 6" preserveAspectRatio="none">
    <rect width="1200" height="6" fill="url(#zz)"/>
  </svg>
</section>

<section>
  <div class="abs rule" style="top:1682px"></div>
  <div class="abs label" style="top:1672px">BLOG</div>
  <h2 class="abs title" style="top:1694px">Latest from our blog</h2>
  <div class="abs sq-arrows" style="left:916px;top:1678px">
    <div><svg width="8" height="8" viewBox="0 0 8 8"><path d="M5.5 1 2.5 4l3 3" fill="none" stroke="#fff" stroke-width="1.4"/></svg></div>
    <div><svg width="8" height="8" viewBox="0 0 8 8"><path d="M2.5 1l3 3-3 3" fill="none" stroke="#fff" stroke-width="1.4"/></svg></div>
  </div>

  <article class="abs post" style="left:234px">
    <div class="photo" role="img" aria-label="Photo of an ornate golden cross" style="background:linear-gradient(160deg,#5a4a2a,#b89248 50%,#3a2a1a)"><span class="badge">03 Aug, 2018 <span>💬 10</span></span></div>
    <h3>LOREM IPSUM DOLOR</h3>
    <p>Lorem ipsum dolor sit amet, consectetur adipiscing elit. Quisque iaculis elementum eleifend. Cras malesuada vitae enim id imperdiet. Vestibulum vestibulum egestas.</p>
    <div class="more">READ MORE</div>
  </article>
  <article class="abs post" style="left:484px">
    <div class="photo" role="img" aria-label="Photo of a closed leather bible" style="background:linear-gradient(160deg,#c8b8a8,#3a2a24 50%,#8a6a58)"><span class="badge">03 Aug, 2018 <span>💬 10</span></span></div>
    <h3>LOREM IPSUM DOLOR</h3>
    <p>Lorem ipsum dolor sit amet, consectetur adipiscing elit. Quisque iaculis elementum eleifend. Cras malesuada vitae enim id imperdiet. Vestibulum vestibulum egestas.</p>
    <div class="more">READ MORE</div>
  </article>
  <article class="abs post" style="left:734px">
    <div class="photo" role="img" aria-label="Photo of a stained glass window" style="background:linear-gradient(160deg,#7a2a1a,#c4a070 45%,#2a4a6a)"><span class="badge">03 Aug, 2018 <span>💬 10</span></span></div>
    <h3>LOREM IPSUM DOLOR</h3>
    <p>Lorem ipsum dolor sit amet, consectetur adipiscing elit. Quisque iaculis elementum eleifend. Cras malesuada vitae enim id imperdiet. Vestibulum vestibulum egestas.</p>
    <div class="more">READ MORE</div>
  </article>
</section>

<footer>
  <div class="abs foot-band"></div>
  <div class="abs newsletter"></div>
  <div class="abs brand foot-brand"><span>Lanternfield<br>Collective</span></div>
  <svg class="abs" style="left:487px;top:2104px" width="12" height="9" viewBox="0 0 12 9"><rect width="12" height="9" fill="#d8d4e6"/><path d="M0 0l6 5 6-5" fill="none" stroke="#3a3060" stroke-width="1"/></svg>
  <div class="abs mail-ph">Your Mail Here</div>
  <div class="abs submit">SUBMIT ▸</div>
  <div class="abs socials"><span></span><span></span><span></span><span></span><span></span></div>

  <div class="abs foot-main"></div>
  <h4 class="abs foot-head" style="left:235px">CONTACT US</h4>
  <p class="abs foot-text" style="left:235px;top:2230px">P.O. Box 48120<br>Millbrook, Oregon 97005-0120</p>
  <p class="abs foot-text" style="left:235px;top:2282px">T: 1 (555) 018-2740</p>
  <div class="abs btn-sq" style="left:235px;top:2320px;background:var(--sky)">
    <svg width="16" height="14" viewBox="0 0 16 14"><path d="M8 3.5C7 1 3.5 1 3.5 4c0 2.5 4.5 5 4.5 5s4.5-2.5 4.5-5c0-3-3.5-3-4.5-.5zM1 12h5l3 1 6-2" fill="none" stroke="#fff" stroke-width="1"/></svg>
    DONATE
  </div>
  <div class="abs vline" style="left:466px"></div>
  <h4 class="abs foot-head" style="left:489px">PHOTO FEED</h4>
  <div class="abs feed">
    <div role="img" aria-label="Photo thumbnail" style="background:#5a4a48"></div>
    <div role="img" aria-label="Photo thumbnail" style="background:#7a5040"></div>
    <div role="img" aria-label="Photo thumbnail" style="background:#c8c4c8"></div>
    <div role="img" aria-label="Photo thumbnail" style="background:#8a7a6a"></div>
    <div role="img" aria-label="Photo thumbnail" style="background:#d8a890"></div>
    <div role="img" aria-label="Photo thumbnail" style="background:#a8b0b8"></div>
    <div role="img" aria-label="Photo thumbnail" style="background:#a07848"></div>
    <div role="img" aria-label="Photo thumbnail" style="background:#6a98c0"></div>
  </div>
  <div class="abs vline" style="left:735px"></div>
  <h4 class="abs foot-head" style="left:767px">USEFUL LINKS</h4>
  <ul class="abs links">
    <li>Home</li><li>About Us</li><li>Projects</li><li>Newsletter &amp; Reports</li><li>Media</li><li>What's New</li><li>Donation</li><li>Contact Us</li>
  </ul>
  <div class="abs hline"></div>
  <p class="abs copy">Copyright © 2018 Lanternfield Collective. All Rights Reserved</p>
</footer>

</body>
</html>
```